Marlowe Consulting Cover 2 - Bright Ledger

Marlowe Consulting is a business consulting firm. We will publish a series of four thought leadership pieces online and via PDF. The second of the series is attached to this project. We need an eye-catching cover page with a back page that keeps with our branding. The document attached is in the final draft, and the cover and pack pages are placeholders only. You can find more about our branding and style on our website www.marloweconsulting.com.au. The other three projects can be found here with a similar brief, and you are welcome to submit a design for all 4.

```html
<!DOCTYPE html>
<html lang="en">
<head>
<meta charset="utf-8">
<title>Marlowe Consulting – Bright Ledger cover and back page</title>
<link href="https://fonts.googleapis.com/css2?family=Poppins:wght@400;500;600&display=swap" rel="stylesheet">
<style>
  :root {
    --stage: #9d9d9d;
    --paper: #f1f1f3;
    --mist: #dfe4e8;
    --band: #e4e7eb;
    --orange: #f7941d;
    --blue: #00aeef;
    --navy: #2d3a4a;
    --photo-light: #8ea6bf;
    --photo-dark: #6d7378;
  }
  * { margin: 0; padding: 0; box-sizing: border-box; }
  html, body { width: 1200px; height: 848px; overflow: hidden; background: var(--stage); }
  body { font-family: "Poppins", sans-serif; color: var(--navy); }
  .canvas { position: relative; width: 1200px; height: 848px; }
  .artwork { position: absolute; inset: 0; width: 1200px; height: 848px; }
  .text { position: absolute; white-space: nowrap; }

  .brand { display: flex; align-items: center; gap: 14px; position: absolute; }
  .brand-dot { border-radius: 50%; background: var(--orange); flex: none; }
  .brand-name { font-weight: 600; color: var(--navy); line-height: 1.05; }

  .cover-brand { left: 67px; top: 72px; }
  .cover-brand .brand-dot { width: 40px; height: 40px; }
  .cover-brand .brand-name { font-size: 19px; }

  .cover-title { left: 67px; top: 148px; font-size: 45px; font-weight: 600; color: var(--orange); }
  .cover-subtitle { left: 67px; top: 213px; font-size: 32px; font-weight: 500; line-height: 41px; }
  .cover-tagline { left: 67px; top: 307px; font-size: 18px; font-weight: 500; }

  .web { display: flex; align-items: center; gap: 7px; font-size: 15px; font-weight: 500; }
  .web svg { width: 14px; height: 14px; }
  .cover-web { left: 277px; top: 770px; }

  .back-brand { left: 653px; top: 62px; }
  .back-brand .brand-dot { width: 70px; height: 70px; }
  .back-brand .brand-name { font-size: 28px; }

  .contact-heading { left: 653px; top: 190px; font-size: 35px; font-weight: 600; color: var(--orange); }
  .contact-intro { left: 653px; top: 256px; font-size: 20px; font-weight: 500; line-height: 27px; }
  .contact-intro strong { font-weight: 600; }

  .person { left: 653px; }
  .person-name { font-size: 21px; font-weight: 600; color: var(--orange); line-height: 26px; }
  .person-role { font-size: 12px; font-weight: 600; color: var(--blue); line-height: 16px; margin-bottom: 6px; }
  .person-line { font-size: 13px; line-height: 18px; }
  .person-first { top: 357px; }
  .person-second { top: 464px; }

  .follow { left: 653px; top: 775px; display: flex; align-items: center; gap: 14px; font-size: 12px; font-weight: 600; }
  .social { width: 15px; height: 15px; background: var(--navy); border-radius: 2px; }
  .back-web { left: 897px; top: 774px; }
</style>
</head>
<body>
<main class="canvas">
  <svg class="artwork" viewBox="0 0 900 636" aria-hidden="false">
    <defs>
      <linearGradient id="photo-tone" x1="0" y1="0" x2="1" y2="1">
        <stop offset="0" stop-color="var(--photo-light)"/>
        <stop offset="1" stop-color="var(--photo-dark)"/>
      </linearGradient>
    </defs>

    <!-- Cover page -->
    <g class="cover-page">
      <rect x="22" y="22" width="418" height="592" fill="var(--paper)"/>
      <rect x="22" y="22" width="418" height="383" fill="var(--mist)"/>
      <rect x="383" y="22" width="14" height="592" fill="var(--blue)"/>
      <g class="cover-bars">
        <rect x="45" y="403" width="10" height="211" fill="var(--blue)"/>
        <rect x="75" y="443" width="10" height="171" fill="var(--orange)"/>
        <rect x="105" y="483" width="10" height="131" fill="var(--blue)"/>
        <rect x="135" y="523" width="10" height="91" fill="var(--orange)"/>
      </g>
      <path d="M120 410 A135 135 0 0 0 255 545" fill="none" stroke="var(--blue)" stroke-width="14"/>
      <path d="M120 410 A135 135 0 0 1 390 410 L390 614" fill="none" stroke="var(--orange)" stroke-width="14"/>
      <circle cx="255" cy="410" r="118" fill="url(#photo-tone)" role="img" aria-label="Photograph looking up at a concrete office building against a blue sky"/>
    </g>

    <!-- Back page -->
    <g class="back-page">
      <rect x="460" y="22" width="420" height="592" fill="var(--paper)"/>
      <polygon points="460,22 560,22 460,130" fill="var(--mist)"/>
      <polygon points="880,22 880,70 640,614 596,614" fill="var(--band)"/>
      <polygon points="880,22 880,330 725,482" fill="var(--orange)"/>
      <polygon points="880,342 880,614 610,614" fill="var(--blue)"/>
    </g>
  </svg>

  <!-- Cover text -->
  <div class="brand cover-brand">
    <span class="brand-dot"></span>
    <span class="brand-name">Marlowe<br>Consulting</span>
  </div>
  <h1 class="text cover-title">Bright Ledger:</h1>
  <p class="text cover-subtitle">Partnering with funds<br>to scale your business.</p>
  <p class="text cover-tagline">Bridging valuation gaps in fund raising</p>
  <p class="text web cover-web">
    <svg viewBox="0 0 16 16" fill="none" stroke="currentColor" stroke-width="1.5"><circle cx="8" cy="8" r="6.5"/><ellipse cx="8" cy="8" rx="2.8" ry="6.5"/><line x1="1.5" y1="8" x2="14.5" y2="8"/></svg>
    marloweconsulting.com.au
  </p>

  <!-- Back page text -->
  <div class="brand back-brand">
    <span class="brand-dot"></span>
    <span class="brand-name">Marlowe<br>Consulting</span>
  </div>
  <h2 class="text contact-heading">Contact us</h2>
  <p class="text contact-intro">Find out how <strong>Marlowe Consulting</strong><br>can help build your company<br>into a market leader today.</p>

  <div class="text person person-first">
    <p class="person-name">Edmund Marlowe</p>
    <p class="person-role">Managing Director</p>
    <p class="person-line">Mobile: +61 400 318 264</p>
    <p class="person-line">Email: edmund@marloweconsulting.com.au</p>
  </div>
  <div class="text person person-second">
    <p class="person-name">Julian Marlowe</p>
    <p class="person-role">Managing Director</p>
    <p class="person-line">Mobile: +61 400 572 819</p>
    <p class="person-line">Email: julian@marloweconsulting.com.au</p>
  </div>

  <div class="text follow">
    <span>Follow us</span>
    <span class="social" aria-label="Social profile"></span>
    <span class="social" aria-label="Social profile"></span>
  </div>
  <p class="text web back-web">
    <svg viewBox="0 0 16 16" fill="none" stroke="currentColor" stroke-width="1.5"><circle cx="8" cy="8" r="6.5"/><ellipse cx="8" cy="8" rx="2.8" ry="6.5"/><line x1="1.5" y1="8" x2="14.5" y2="8"/></svg>
    marloweconsulting.com.au
  </p>
</main>
</body>
</html>
```